We Brookmeade Grace Fellowship Church Need a Post card that will be an invite for just one Sunday...which is THE LAST SUNDAY of the year. We are a small church but we are pushing to have 150 the last Sunday of 2014 which is December 28th 2014...Our service will begin at 10 a.m. We will have a meal to follow service. I would like for you to help me with a nice back ground that will grab peoples attention.. and also I like to keep the same theme and make some folding Business cards to send people thank you for visiting. and also a regular size business card to slip inside that and to hand out on a daily basis... Our Web site is www.Brookmeade1stFellowship.example all our info is on there and you can kind of see our theme we are going with. and also I was wondering is it possible to push the post Cards THE LAST SUNDAY CARD so we can start handing them out... we like to have 500 of those and say 1000 Folding business cards and 1000 regular Busyness cards..

Nmae . Pastor Dale Orwin, # 555-274-8106

```html
<!DOCTYPE html>
<html lang="en">
<head>
<meta charset="utf-8">
<title>The Last Sunday – Postcard and Business Cards</title>
<link href="https://fonts.googleapis.com/css2?family=Oswald:wght@500&family=Roboto+Condensed:wght@400;700&family=Lato:wght@400&display=swap" rel="stylesheet">
<style>
  :root {
    --stage: #000000;
    --teal: #1f7fa6;
    --ink: #111111;
    --brand-ink: #3a3f44;
    --panel: rgba(255, 255, 255, 0.62);
    --sky-top: #8fc3ec;
    --sky-mid: #eef5f6;
    --sun: #f2f0a8;
    --meadow: #8ebf3c;
    --meadow-deep: #3f8a24;
    --card-white: #ffffff;
  }
  * { margin: 0; padding: 0; box-sizing: border-box; }
  html, body {
    width: 1200px; height: 1133px; overflow: hidden;
    background: var(--stage);
  }
  .canvas { position: relative; width: 1200px; height: 1133px; }

  .meadow-photo {
    position: absolute;
    background: linear-gradient(180deg, var(--sky-top) 0%, var(--sky-mid) 30%, var(--sun) 48%, var(--meadow) 65%, var(--meadow-deep) 100%);
  }

  /* Postcard */
  .postcard { position: absolute; left: 214px; top: 40px; width: 752px; height: 578px; overflow: hidden; }
  .postcard .meadow-photo { inset: 0; }
  .invite-panel {
    position: absolute; left: 63px; top: 63px; width: 626px; height: 465px;
    background: var(--panel);
    box-shadow: 0 2px 8px rgba(0,0,0,0.12);
    text-align: center;
  }
  .page-curl { position: absolute; right: -2px; top: -2px; }

  .brand {
    display: flex; align-items: center; justify-content: center; gap: 9px;
    font-family: "Lato", sans-serif; font-weight: 400; color: var(--brand-ink);
  }
  .brand-dot { border-radius: 50%; background: var(--teal); flex: none; }

  .invite-panel .brand { margin-top: 36px; font-size: 19px; }
  .invite-panel .brand-dot { width: 14px; height: 14px; }

  .event-title {
    font-family: "Oswald", sans-serif; font-weight: 500; color: var(--teal);
    font-size: 64px; line-height: 1; letter-spacing: -0.5px;
    margin-top: 36px; transform: scaleY(1.08);
  }
  .event-invite {
    font-family: "Oswald", sans-serif; font-weight: 500; color: var(--teal);
    font-size: 34px; line-height: 1; margin-top: 20px;
  }
  .event-details {
    font-family: "Roboto Condensed", sans-serif; font-size: 19.5px; line-height: 25px;
    color: var(--ink); margin-top: 12px;
  }
  .event-contact {
    font-family: "Roboto Condensed", sans-serif; font-weight: 700; font-size: 19.5px; line-height: 25px;
    color: var(--ink); margin-top: 15px;
  }

  /* Business card front */
  .card-front { position: absolute; left: 139px; top: 654px; width: 476px; height: 290px; overflow: hidden; }
  .card-front .meadow-photo { inset: 0; }
  .card-front .brand { position: absolute; left: 0; right: 0; top: 108px; font-size: 19px; }
  .card-front .brand-dot { width: 14px; height: 14px; }

  /* Business card back */
  .card-back {
    position: absolute; left: 534px; top: 810px; width: 476px; height: 290px;
    background: var(--card-white); text-align: center;
  }
  .card-back .brand { position: absolute; left: 0; right: 0; top: 72px; font-size: 19px; }
  .card-back .brand-dot { width: 14px; height: 14px; }
  .card-contact {
    position: absolute; left: 0; right: 0; top: 182px;
    font-family: "Roboto Condensed", sans-serif; font-size: 15.5px; line-height: 20.5px; color: var(--ink);
  }
  .accent-bar { position: absolute; left: 118px; bottom: 0; width: 239px; height: 14px; background: var(--teal); }
</style>
</head>
<body>
<main class="canvas">

  <section class="postcard">
    <div class="meadow-photo" role="img" aria-label="Sunlit meadow of white daisies and tall grass under a bright blue sky with soft clouds"></div>
    <div class="invite-panel">
      <svg class="page-curl" width="110" height="110" viewBox="0 0 110 110" aria-hidden="true">
        <path d="M0 2 H108 V110 C98 80 92 60 74 52 C92 56 100 40 84 26 C66 10 40 8 0 2 Z" fill="#ffffff"/>
        <path d="M60 2 C86 4 104 16 100 38 C96 52 84 54 74 52 C92 46 96 30 82 20 C72 12 66 6 60 2 Z" fill="#e6e6e6"/>
      </svg>
      <div class="brand"><span class="brand-dot"></span>Brookmeade Grace Fellowship Church</div>
      <h1 class="event-title">THE LAST SUNDAY</h1>
      <p class="event-invite">You are invited.</p>
      <p class="event-details">
        The last Sunday of 2014, December 28th 2014<br>
        Time: 10 A.M.<br>
        2740 Brookmeade Rd. Brookmeade Tn. 38900<br>
        We will have a meal to follow service.
      </p>
      <p class="event-contact">
        555-274-8106<br>
        pastororwinbgfc@example.com<br>
        www.Brookmeade1stFellowship.example
      </p>
    </div>
  </section>

  <section class="card-front">
    <div class="meadow-photo" role="img" aria-label="Sunlit meadow of white daisies and tall grass under a bright blue sky"></div>
    <div class="brand"><span class="brand-dot"></span>Brookmeade Grace Fellowship Church</div>
  </section>

  <section class="card-back">
    <div class="brand"><span class="brand-dot"></span>Brookmeade Grace Fellowship Church</div>
    <p class="card-contact">
      555-274-8106<br>
      pastororwinbgfc@example.com<br>
      www.Brookmeade1stFellowship.example
    </p>
    <div class="accent-bar"></div>
  </section>

</main>
</body>
</html>
```